Graphic Design For Website Banner + 4 Product Images - More Work To Follow

We are in the process of launching a new website. I need to design a banner for the homepage, as well as some graphics for my product images.

Please find attached -

1) My current logo.
2) Banner Sample + Product Image Sample - both of these are a screenshot from a common website that I like the design and style of.
3) Colour Scheme Sample 1 - saved image showing colour scheme for BrushOtter that I like.
4) Colour Scheme Sample 2 - Saved image showing colour scheme for Plivo that I like.
5) Sample 1-4 - These are colour palette samples I created online showing what I like.
6) 4 blank product images to show what is required in the design.

To summarise I'll like to create a banner design and product images similar to what's been attached and have a consistent colour theme throughout. I'm happy to adjust the colours in my logo to match the final designs.

To begin with I'll be requesting 1 banner design and 4 product images. I'll have more work for the successful designer.

Banner -
Size to be 950x300. To contain the following wording -
Quality Printing
Offset|Digital|Wideformat
Deal Direct & Save
Possibly include some product images like the sample banner attached.

Product Images -
Size to be 263x263
1) Business Cards
2) Folded Brochures
3) Flyers
4) Presentation Folders
I've attached blank sample images of all 4 for your reference.

Please feel free to ask any questions as I'm happy to give further direction.

Target Market(s)

We are a commercial Printer offering a range of printed products

Font styles to use
Serif
Sans Serif

Colors
34a6d7
33b8a4
3277b5
86cfc7
86cae7
85acd3
00a990
0393ce
0255a3

```html
<!DOCTYPE html>
<html lang="en">
<head>
<meta charset="utf-8">
<title>Inkwell Press – Product Banners</title>
<link href="https://fonts.googleapis.com/css2?family=Montserrat:wght@500;600;700;800&display=swap" rel="stylesheet">
<style>
  :root {
    --page-bg: #1f1c35;
    --banner-green: #2ee37a;
    --banner-teal: #22c3a0;
    --banner-blue: #1e8fd2;
    --white: #ffffff;
    --accent-lime: #d4f56a;
    --button-text: #1a6f8f;
    --mock-light: #f4f6f8;
    --mock-shade: #cfd8e0;
  }
  * { margin: 0; padding: 0; box-sizing: border-box; }
  html, body {
    width: 896px; height: 1200px; overflow: hidden;
    background: var(--page-bg);
    font-family: "Montserrat", sans-serif;
  }
  .sheet { position: relative; width: 896px; height: 1200px; }

  .product-row { position: absolute; left: 0; width: 896px; height: 245px; }
  .product-label {
    position: absolute; left: 45px; top: 50%;
    transform: translate(-50%, -50%) rotate(-90deg);
    color: var(--white); font-weight: 700; font-size: 25px;
    letter-spacing: 1px; white-space: nowrap;
  }
  .banner {
    position: absolute; left: 90px; top: 0; width: 782px; height: 245px;
    background: linear-gradient(125deg, var(--banner-green) 0%, var(--banner-teal) 45%, var(--banner-blue) 100%);
    overflow: hidden;
  }
  .brand {
    position: absolute; left: 88px; top: 36px;
    color: var(--white); font-weight: 800; font-size: 19px;
    line-height: 21px; letter-spacing: 1px;
  }
  .headline {
    position: absolute; left: 88px; top: 100px;
    color: var(--white); font-weight: 600; font-size: 16px; letter-spacing: 0.5px;
  }
  .services {
    position: absolute; left: 88px; top: 122px;
    color: var(--white); font-weight: 800; font-size: 18px; letter-spacing: 0.5px;
  }
  .tagline {
    position: absolute; left: 88px; top: 148px;
    color: var(--accent-lime); font-weight: 700; font-size: 11px; letter-spacing: 0.5px;
  }
  .read-more {
    position: absolute; left: 88px; top: 180px; width: 108px; height: 32px;
    background: var(--white); color: var(--button-text);
    font-weight: 700; font-size: 11px; letter-spacing: 0.5px;
    display: flex; align-items: center; justify-content: center;
  }
  .product-visual {
    position: absolute;
    background: linear-gradient(150deg, var(--mock-light) 0%, var(--mock-shade) 100%);
    box-shadow: 0 14px 24px rgba(0, 0, 0, 0.18);
  }
  .visual-flyers { left: 470px; top: 22px; width: 250px; height: 200px; transform: rotate(-8deg); }
  .visual-brochure { left: 480px; top: 30px; width: 220px; height: 185px; transform: skewY(-14deg); }
  .visual-folder { left: 440px; top: 55px; width: 290px; height: 130px; }
  .visual-cards { left: 470px; top: 40px; width: 230px; height: 165px; border-radius: 14px; transform: rotate(-12deg); }
</style>
</head>
<body>
<main class="sheet">

  <section class="product-row" style="top:30px">
    <div class="product-label">PRODUCT 01</div>
    <div class="banner">
      <div class="brand">INKWELL<br>PRESS</div>
      <div class="headline">QUALITY PRINTING</div>
      <div class="services">OFFSET | DIGITAL | WIDEFORMAT</div>
      <div class="tagline">DEAL DIRECT &amp; SAVE</div>
      <div class="read-more">READ MORE</div>
      <div class="product-visual visual-flyers" role="img" aria-label="Stack of printed flyers"></div>
    </div>
  </section>

  <section class="product-row" style="top:328px">
    <div class="product-label">PRODUCT 02</div>
    <div class="banner">
      <div class="brand">INKWELL<br>PRESS</div>
      <div class="headline">QUALITY PRINTING</div>
      <div class="services">OFFSET | DIGITAL | WIDEFORMAT</div>
      <div class="tagline">DEAL DIRECT &amp; SAVE</div>
      <div class="read-more">READ MORE</div>
      <div class="product-visual visual-brochure" role="img" aria-label="Folded tri-fold brochure"></div>
    </div>
  </section>

  <section class="product-row" style="top:626px">
    <div class="product-label">PRODUCT 03</div>
    <div class="banner">
      <div class="brand">INKWELL<br>PRESS</div>
      <div class="headline">QUALITY PRINTING</div>
      <div class="services">OFFSET | DIGITAL | WIDEFORMAT</div>
      <div class="tagline">DEAL DIRECT &amp; SAVE</div>
      <div class="read-more">READ MORE</div>
      <div class="product-visual visual-folder" role="img" aria-label="Open presentation folder"></div>
    </div>
  </section>

  <section class="product-row" style="top:924px">
    <div class="product-label">PRODUCT 04</div>
    <div class="banner">
      <div class="brand">INKWELL<br>PRESS</div>
      <div class="headline">QUALITY PRINTING</div>
      <div class="services">OFFSET | DIGITAL | WIDEFORMAT</div>
      <div class="tagline">DEAL DIRECT &amp; SAVE</div>
      <div class="read-more">READ MORE</div>
      <div class="product-visual visual-cards" role="img" aria-label="Pair of business cards"></div>
    </div>
  </section>

</main>
</body>
</html>
```